Business Card Design

I need a business card for my rental business. The business is named:
Hire a Vorlatrike Brenmoor
www.hireavorlatrikebrenmoor.example
(555) 014-2937
This will be a business card that I will leave at other businesses as advertisement so it needs to have the name, website, and phone number.
Please feel free to be creative. This is a new business so I have no designs.
Thank you very much for your time and I look forward to receiving your designs
Target Market(s)
Local rental customers
Industry/Entity Type
Business
Contact Information for Business Card
Please check out my website:
Other font styles liked:
- anything creative
Colors
Designer to choose colors to be used in the design.
Requirements
Must have
- Business name, phone, website. Rentals available hourly or daily. Book online

```html
<!DOCTYPE html>
<html lang="en">
<head>
<meta charset="utf-8">
<title>Hire a Vorlatrike Brenmoor — Business Card</title>
<link rel="stylesheet" href="https://fonts.googleapis.com/css2?family=Open+Sans:wght@400;600;700&display=swap">
<style>
  :root {
    --backdrop: #3a3431;
    --card: #0e0e0e;
    --card-edge: #1c1c1c;
    --divider: #2a2a2a;
    --brand-grey: #8d8d8d;
    --brand-silver: #c9c9c9;
    --name-grey: #7a7a7a;
    --text-light: #e6e6e6;
    --text-soft: #a8a8a8;
    --icon-grey: #9a9a9a;
  }
  * { margin: 0; padding: 0; box-sizing: border-box; }
  html, body {
    width: 1200px;
    height: 900px;
    overflow: hidden;
    background: var(--backdrop);
    font-family: "Open Sans", Arial, sans-serif;
  }
  .canvas {
    position: relative;
    width: 1200px;
    height: 900px;
  }
  .card {
    position: absolute;
    top: 300px;
    width: 520px;
    height: 297px;
    background: var(--card);
    border: 1px solid var(--card-edge);
    border-radius: 3px;
    overflow: hidden;
  }
  .card--back { left: 50px; }
  .card--front { left: 630px; }

  .brand {
    font-weight: 700;
    text-transform: uppercase;
    line-height: 1.02;
    letter-spacing: 0.5px;
  }
  .card--back .brand {
    position: absolute;
    left: 28px;
    top: 102px;
    width: 180px;
    font-size: 26px;
    color: var(--brand-grey);
  }
  .card--front .brand {
    position: absolute;
    left: 0;
    right: 0;
    top: 84px;
    text-align: center;
    font-size: 38px;
    color: var(--brand-silver);
  }

  .divider {
    position: absolute;
    left: 216px;
    top: 40px;
    width: 1px;
    height: 216px;
    background: var(--divider);
  }
  .contact {
    position: absolute;
    left: 234px;
    top: 52px;
    width: 270px;
  }
  .contact__name {
    font-size: 16px;
    font-weight: 600;
    color: var(--name-grey);
  }
  .contact__title {
    font-size: 12px;
    color: var(--text-light);
    margin-bottom: 20px;
  }
  .contact__list { list-style: none; }
  .contact__item {
    display: flex;
    align-items: center;
    gap: 8px;
    font-size: 11.5px;
    color: var(--text-light);
    line-height: 19px;
    white-space: nowrap;
  }
  .contact__icon {
    width: 11px;
    height: 11px;
    flex: none;
    fill: var(--icon-grey);
  }
  .contact__offer {
    margin-top: 18px;
    font-size: 10.5px;
    line-height: 15px;
    color: var(--text-soft);
  }
</style>
</head>
<body>
<main class="canvas">
  <section class="card card--back" aria-label="Business card, contact side">
    <p class="brand">Hire a<br>Vorlatrike<br>Brenmoor</p>
    <div class="divider"></div>
    <div class="contact">
      <p class="contact__name">Dorian Kessel</p>
      <p class="contact__title">Managing Director</p>
      <ul class="contact__list">
        <li class="contact__item">
          <svg class="contact__icon" viewBox="0 0 24 24" aria-hidden="true"><path d="M6.6 10.8a15.1 15.1 0 0 0 6.6 6.6l2.2-2.2a1 1 0 0 1 1-.25 11.4 11.4 0 0 0 3.6.57 1 1 0 0 1 1 1V20a1 1 0 0 1-1 1A17 17 0 0 1 3 4a1 1 0 0 1 1-1h3.5a1 1 0 0 1 1 1c0 1.25.2 2.45.57 3.6a1 1 0 0 1-.25 1z"/></svg>
          (555) 014-2937
        </li>
        <li class="contact__item">
          <svg class="contact__icon" viewBox="0 0 24 24" aria-hidden="true"><path d="M2 5h20v14H2z M4 7v.4l8 5 8-5V7z" fill-rule="evenodd"/></svg>
          info@hireavorlatrikebrenmoor.example
        </li>
        <li class="contact__item">
          <svg class="contact__icon" viewBox="0 0 24 24" aria-hidden="true"><circle cx="12" cy="12" r="9" fill="none" stroke="#9a9a9a" stroke-width="2"/><path d="M3 12h18M12 3c3 3 3 15 0 18M12 3c-3 3-3 15 0 18" fill="none" stroke="#9a9a9a" stroke-width="1.6"/></svg>
          www.hireavorlatrikebrenmoor.example
        </li>
      </ul>
      <p class="contact__offer">Rentals available hourly or daily.<br>Book online</p>
    </div>
  </section>

  <section class="card card--front" aria-label="Business card, brand side">
    <p class="brand">Hire a<br>Vorlatrike<br>Brenmoor</p>
  </section>
</main>
</body>
</html>
```